Brand of baby products for bath & bedding items needs new packaging concept

Our brand is called Cradle Nook and we make products for bath, bedding, maternity body pillows and disposable baby bibs and change mats. We sell to baby stores and retail stores across North America and Europe. Our positioning is mid/high end and we need a new modern look that is simple. We tend to include too much text and overload our packaging. It should be modern and clean. Our current background pattern is a bit too loud and makes things look cluttered. We want a consistent look that can be used across all of our products. It can however have slight differences to categorize the items (ie: all bath items have a particular colour stripe at the bottom to help group them). Please visit out website: www.tinyhavenmarket.example to see more details on the current range and branding. We have products packaged in bags, some in boxes etc... I've also attached our brand presentation. The final design should communicate quality and comfort.

Target Market(s)

Baby products that appeal to moms and dads

Industry/Entity Type

Baby

Colors
876aae
85acd3
5c5c5c
9d9d9d
33b8a4
b768aa
87cfc6

Requirements
Should not have
• It should not be gender specific. It needs to include colours that appeal to both boys and girls. Blue is OK but pink is not. I also don't like yellow or orange. I like "soft" and light colours.

```html
<!DOCTYPE html>
<html lang="en">
<head>
<meta charset="utf-8">
<title>Cradle Nook – Toddler Pillow Label</title>
<link rel="stylesheet" href="https://fonts.googleapis.com/css2?family=Comfortaa:wght@400;700&family=Anton&family=Nunito:wght@400;700;800&display=swap">
<style>
  :root {
    --cyan: #1fc1e0;
    --purple: #876aae;
    --grey: #9d9d9d;
    --ink: #111111;
    --white: #ffffff;
    --page: #f4f4f4;
  }
  html, body {
    margin: 0;
    padding: 0;
    width: 1200px;
    height: 1200px;
    overflow: hidden;
    background: var(--page);
  }
  .canvas {
    position: relative;
    width: 1200px;
    height: 1200px;
  }
  .label {
    position: absolute;
    left: 0;
    top: 209px;
    width: 1082px;
    height: 705px;
    background: var(--white);
    overflow: hidden;
    transform: scale(1.109);
    transform-origin: top left;
  }
  .wave {
    position: absolute;
    inset: 0;
    width: 1082px;
    height: 705px;
  }
  .brand {
    position: absolute;
    left: 146px;
    top: 82px;
    font-family: "Nunito", sans-serif;
    font-weight: 800;
    font-size: 34px;
    color: var(--purple);
    letter-spacing: -0.5px;
    display: flex;
    align-items: center;
    gap: 8px;
  }
  .brand-dot {
    width: 12px;
    height: 12px;
    border-radius: 50%;
    background: var(--purple);
  }
  .age-badge {
    position: absolute;
    left: 860px;
    top: 32px;
    width: 120px;
    height: 120px;
    border-radius: 50%;
    background: var(--white);
    display: flex;
    flex-direction: column;
    align-items: center;
    justify-content: center;
    font-family: "Anton", sans-serif;
    color: var(--ink);
    line-height: 1;
  }
  .age-badge .age { font-size: 42px; }
  .age-badge .unit { font-size: 22px; margin-top: 2px; }
  .photo {
    position: absolute;
    left: 580px;
    top: 268px;
    width: 502px;
    height: 437px;
    border-top-left-radius: 320px 260px;
    background: linear-gradient(150deg, #f6f6f6 0%, #eceae8 38%, #e8c9b4 62%, #a7704b 85%, #e9e4dc 100%);
  }
  .sub-brand {
    position: absolute;
    left: 640px;
    top: 282px;
    font-family: "Comfortaa", sans-serif;
    font-weight: 700;
    font-size: 30px;
    color: #c9c9c9;
  }
  .title {
    position: absolute;
    left: 90px;
    top: 292px;
    margin: 0;
    font-family: "Comfortaa", sans-serif;
    font-weight: 700;
    font-size: 100px;
    line-height: 86px;
    color: var(--cyan);
    letter-spacing: 4px;
  }
  .tagline {
    position: absolute;
    left: 110px;
    top: 520px;
    margin: 0;
    font-family: "Comfortaa", sans-serif;
    font-size: 23px;
    color: var(--ink);
  }
  .rule {
    position: absolute;
    left: 7px;
    top: 644px;
    width: 388px;
    height: 3px;
    background: linear-gradient(90deg, rgba(31,193,224,0.2), var(--cyan));
  }
  .feature {
    position: absolute;
    left: 398px;
    top: 508px;
    width: 262px;
    height: 262px;
    border-radius: 50%;
    background: var(--cyan);
    border: 4px solid var(--white);
    overflow: hidden;
  }
  .feature-visual {
    position: absolute;
    left: 22px;
    top: 22px;
    width: 105px;
    height: 85px;
    border-radius: 10px;
    background: linear-gradient(135deg, #f3efe6, #ddd4c3);
    transform: rotate(12deg);
  }
  .feature-text {
    position: absolute;
    right: 18px;
    top: 135px;
    width: 120px;
    margin: 0;
    font-family: "Nunito", sans-serif;
    font-size: 9.5px;
    line-height: 1.35;
    color: var(--white);
    text-align: right;
  }
</style>
</head>
<body>
<div class="canvas">
  <section class="label">
    <svg class="wave" viewBox="0 0 1082 705" aria-hidden="true">
      <path fill="var(--cyan)" d="M0,125 C110,105 220,160 257,222 C300,200 360,195 402,208 C470,100 620,55 742,62 C760,40 770,15 778,0 L1082,0 L1082,42 C1030,45 985,80 975,100 C935,130 920,170 905,218 C850,225 790,240 762,262 C650,240 450,240 357,282 C250,250 100,270 0,350 Z"/>
    </svg>

    <div class="brand"><span class="brand-dot"></span>Cradle Nook</div>

    <div class="age-badge"><span class="age">24+</span><span class="unit">months</span></div>

    <div class="photo" role="img" aria-label="Photo of a toddler sleeping peacefully on a soft cream pillow"></div>
    <div class="sub-brand">Snug Haven</div>

    <h1 class="title">toddler<br>pillow</h1>
    <p class="tagline">with pillow case included</p>
    <div class="rule"></div>

    <div class="feature">
      <div class="feature-visual" role="img" aria-label="Illustration of the ventilated pillow with airflow arrows"></div>
      <p class="feature-text">Air ventilation keeps pillow cool and comfortable<br>La ventilation garde l'oreiller frais et confortable.</p>
    </div>
  </section>
</div>
</body>
</html>
```